Business Card Design

My company is an online based training service targeted at individuals who want to learn how to consistently make money at online tournament poker.

The training takes place online using skype and is extremely easy to use.

Final design should communicate that my business offers online tournament poker coaching from one of the most successful online tournament poker players in Scotland and the UK.

Further information can be found @ http://www.mendmyhand.net/

Industry/Entity Type

Training

Contact Information for Business Card

- 'Learn from one of the best online tournament poker players in Scotland and the UK' (or something similar)
- Previous winnings
Reference: http://www.mendmyhand.net/

Requirements
Must have
• MendMyHand.net
Nice to have
• A similar look or feel to my website (http://www.mendmyhand.net/)

```html
<!DOCTYPE html>
<html lang="en">
<head>
<meta charset="utf-8">
<title>Mend My Hand – Business Card</title>
<link rel="stylesheet" href="https://fonts.googleapis.com/css2?family=Tinos:wght@400;700&display=swap">
<style>
  :root {
    --page: #e9e6e1;
    --ink-dark: #0d0f12;
    --ink-mid: #2a2f36;
    --gold: #f2b01e;
    --gold-light: #ffd45a;
    --gold-deep: #c98a0c;
    --white: #ffffff;
    --grey: #9aa0a6;
    --felt: #1f4a33;
    --felt-dark: #123322;
    --photo-a: #5d6874;
    --photo-b: #1a1e24;
  }
  * { margin: 0; padding: 0; box-sizing: border-box; }
  html, body { width: 1200px; height: 841px; overflow: hidden; }
  body {
    background: var(--page);
    font-family: "Tinos", "Times New Roman", serif;
    display: flex;
    flex-direction: column;
    align-items: center;
    justify-content: center;
    gap: 36px;
  }
  .card {
    position: relative;
    width: 640px;
    height: 366px;
    overflow: hidden;
    box-shadow: 0 6px 18px rgba(0,0,0,.25);
  }

  /* Front */
  .card--front {
    background: radial-gradient(ellipse at 40% 40%, var(--ink-mid), var(--ink-dark) 75%);
  }
  .headline {
    position: absolute;
    top: 20px; left: 30px; right: 30px;
    color: var(--gold);
    font-weight: 700;
    font-size: 19px;
    line-height: 1.3;
    letter-spacing: 2px;
    text-align: center;
  }
  .portrait {
    position: absolute;
    right: 0; top: 95px;
    width: 300px; height: 271px;
    background: radial-gradient(ellipse at 55% 45%, var(--photo-a), var(--photo-b) 75%);
  }
  .brand {
    position: absolute;
    left: 30px; top: 112px;
    display: flex; flex-direction: column; align-items: center;
  }
  .brand__mark {
    width: 34px; height: 34px;
    border-radius: 50%;
    background: var(--gold);
    margin-bottom: 8px;
  }
  .brand__name {
    color: var(--gold);
    font-weight: 700;
    font-size: 32px;
    letter-spacing: 1px;
  }
  .brand__tagline {
    color: var(--white);
    font-weight: 700;
    font-size: 9.5px;
    letter-spacing: .3px;
    margin-top: 2px;
  }
  .social {
    position: absolute;
    left: 30px; top: 222px;
  }
  .social__icons { display: flex; gap: 4px; }
  .social__icon {
    width: 18px; height: 18px;
    background: var(--grey);
    border-radius: 2px;
  }
  .social__label {
    color: var(--gold);
    font-size: 11px;
    letter-spacing: 4px;
    margin-top: 4px;
  }
  .band {
    position: absolute;
    left: 0; bottom: 0;
    width: 640px; height: 120px;
  }
  .url {
    position: absolute;
    left: 0; right: 0; bottom: 28px;
    text-align: center;
    color: var(--ink-dark);
    font-weight: 700;
    font-size: 15px;
    letter-spacing: 7px;
  }

  /* Back */
  .card--back {
    background: radial-gradient(ellipse at 50% 40%, var(--felt), var(--felt-dark) 85%);
  }
  .art {
    position: absolute;
  }
  .art--chips-left {
    left: 40px; top: 26px; width: 150px; height: 100px;
    background: radial-gradient(ellipse, rgba(242,176,30,.55), rgba(180,30,30,.25) 60%, transparent 75%);
  }
  .art--cards {
    left: 280px; top: 34px; width: 150px; height: 100px;
    background: linear-gradient(135deg, #ffffff, #dcdcdc);
    border-radius: 6px;
  }
  .art--chips-right {
    right: 30px; top: 190px; width: 140px; height: 150px;
    background: radial-gradient(ellipse, rgba(242,176,30,.5), rgba(255,255,255,.18) 55%, transparent 75%);
  }
  .back-brand {
    position: absolute;
    left: 0; right: 0; top: 150px;
    text-align: center;
  }
  .back-brand__row {
    display: flex; align-items: center; justify-content: center; gap: 12px;
  }
  .back-brand__name {
    color: var(--gold);
    font-weight: 700;
    font-size: 34px;
    letter-spacing: 2px;
  }
  .back-brand__mark {
    width: 30px; height: 30px;
    border-radius: 50%;
    background: var(--gold);
  }
  .back-brand__tagline {
    color: var(--white);
    font-weight: 700;
    font-size: 11px;
    letter-spacing: .5px;
    margin-top: 4px;
  }
  .back-brand__url {
    color: var(--gold);
    font-style: italic;
    font-size: 16px;
    letter-spacing: 4px;
    margin-top: 6px;
  }
</style>
</head>
<body>

<section class="card card--front">
  <p class="headline">Learn from one of the best online tournament poker players in Scotland and the UK.</p>

  <div class="portrait" role="img" aria-label="Photo of a poker player in a suit holding a chip, with smoke"></div>

  <div class="brand">
    <span class="brand__mark"></span>
    <span class="brand__name">MEND MY HAND</span>
    <span class="brand__tagline">TAKE YOUR GAME TO THE NEXT LEVEL</span>
  </div>

  <div class="social">
    <div class="social__icons">
      <span class="social__icon"></span>
      <span class="social__icon"></span>
      <span class="social__icon"></span>
    </div>
    <p class="social__label">SOCIAL</p>
  </div>

  <svg class="band" viewBox="0 0 640 120" preserveAspectRatio="none" aria-hidden="true">
    <defs>
      <linearGradient id="goldBand" x1="0" y1="0" x2="1" y2="0">
        <stop offset="0" stop-color="var(--gold-deep)"/>
        <stop offset=".5" stop-color="var(--gold-light)"/>
        <stop offset="1" stop-color="var(--gold-deep)"/>
      </linearGradient>
    </defs>
    <path d="M0 14 Q260 -6 640 56 L640 68 Q260 8 0 28 Z" fill="var(--gold)"/>
    <path d="M0 34 Q260 14 640 76 L640 120 L0 120 Z" fill="url(#goldBand)"/>
  </svg>
  <p class="url">www.mendmyhand.net</p>
</section>

<section class="card card--back">
  <div class="art art--chips-left" role="img" aria-label="Scattered poker chips and playing cards"></div>
  <div class="art art--cards" role="img" aria-label="Fanned playing cards"></div>
  <div class="art art--chips-right" role="img" aria-label="Scattered poker chips and playing cards"></div>

  <div class="back-brand">
    <div class="back-brand__row">
      <span class="back-brand__name">MEND MY HAND</span>
      <span class="back-brand__mark"></span>
    </div>
    <p class="back-brand__tagline">TAKE YOUR GAME TO THE NEXT LEVEL</p>
    <p class="back-brand__url">www.mendmyhand.net</p>
  </div>
</section>

</body>
</html>
```